Online CBD and Delta 8 web store

Need a website built with page categories as Delta 8 products, CBD gummies/edibles, Hemp flower/Wax, CBD for pets, CBD vapes/Cartridges, capsules & gel tabs, and Misc. Must have all the items completed as mentioned in the attachment. must have "must be 21+ to enter site" button upon entry. Please put privacy policy and shipping and refund policy as a basic standard template most websites have. I want everything to be just plug in pics and pricing for my products when website is completed and designed. A few cbd sites I like is leafnook.example, qrt-cbd.example,

• my logo and

WEBSITE MUST BE COMPLETE AND HAVE THE FOLLOWING:
___ Privacy Policy
___ Shipping Policy
___ Refund Policy
___ Terms & Conditions
___ Pavo & CoinRidge Logos must be on footer of website
___ Contact Us link or information on the site, including phone number, email and city, state & zip
___ Photos of all products being sold must be posted
___ Pricing for all products must be clearly shown
___ Must have age verification upon entry or at checkout on the site
___ Certificates of Analysis for products must be posted on the site
___ Customers cannot make product claims specific to ailments (for example, stress or anxiety)
___ Disclaimer for “no thc” or “< 0.3% thc content or less” must be posted on the site
___ NWB Disclaimer must be posted on the site:
The statements made regarding these products have not been evaluated by the National Wellness
Bureau. The efficacy of these products has not been confirmed by NWB-approved research.
These products are not intended to diagnose, treat, cure or prevent any disease. All information
presented here is not meant as a substitute for or alternative to information from health care
practitioners. Please consult your health care professional about potential interactions or other
possible complications before using any product. The Federal Food, Drug, and Cosmetic Act require
this notice.

```html
<!DOCTYPE html>
<html lang="en">
<head>
<meta charset="utf-8">
<title>Greenvale CBD Co. – Home</title>
<link href="https://fonts.googleapis.com/css2?family=Montserrat:wght@600;700&family=Fira+Sans:ital,wght@0,400;0,500;0,600;1,400&family=Fira+Sans+Condensed:wght@400&display=swap" rel="stylesheet">
<style>
:root{
  --green:#3f9a2a;
  --green-dark:#1d7a2e;
  --green-deep:#0f6a2b;
  --green-light:#8cc63f;
  --ink:#222;
  --muted:#555;
  --grey-bg:#eeeeef;
  --footer:#262626;
  --white:#fff;
}
*{box-sizing:border-box;margin:0;padding:0}
html,body{width:693px;height:1200px;overflow:hidden;background:var(--white)}
.canvas{width:1456px;height:2540px;transform:scale(.4724);transform-origin:0 0;position:relative;background:var(--white);font-family:"Fira Sans",sans-serif;color:var(--ink)}
.page{position:absolute;top:68px;width:648px;height:2387px;overflow:hidden;background:var(--white);box-shadow:0 0 6px rgba(0,0,0,.12)}
.page--home{left:48px}
.page--gate{left:760px}
.abs{position:absolute}
.center{left:0;right:0;text-align:center}

/* header */
.site-header{top:0;left:0;width:648px;height:88px;background:var(--white)}
.brand{color:var(--green-dark);font-family:"Fira Sans",sans-serif;font-weight:600;font-size:13px;line-height:15px;text-align:center;letter-spacing:1px}
.search{left:400px;top:12px;width:154px;height:25px;border:1.5px solid var(--ink);border-radius:13px;font-size:9px;padding:6px 10px}
.search-btn{position:absolute;right:2px;top:2px;width:19px;height:18px;border-radius:50%;background:var(--green)}
.nav{top:58px;left:309px;display:flex;gap:15px;font-size:8.5px;font-weight:500}
.nav .active{color:var(--green);text-decoration:underline}
.icon-btn{top:53px;width:22px;height:22px;border-radius:50%;border:1.5px solid var(--green)}
.icon-btn.filled{background:var(--green)}

/* hero */
.hero{top:88px;left:0;width:648px;height:320px;background:linear-gradient(180deg,#f6f6f7,#fdfdfd)}
.hero-photo{left:290px;top:0;width:358px;height:250px;background:radial-gradient(ellipse at 60% 55%,#7f9a5a 0,#a9bd8e 35%,#d5e6cf 60%,rgba(255,255,255,0) 75%)}
.hero-title{left:92px;top:90px;font-family:"Montserrat",sans-serif;font-weight:700;font-size:30px;color:var(--green);letter-spacing:1px}
.hero-text{left:93px;top:134px;width:290px;font-size:9.5px;line-height:16px}
.btn{display:inline-block;border-radius:16px;font-family:"Montserrat",sans-serif;font-weight:700;font-size:7.5px;text-align:center;color:var(--white);background:linear-gradient(180deg,var(--green),var(--green-dark))}
.btn--hero{left:93px;top:181px;width:76px;height:30px;line-height:30px}

/* about */
.about{top:362px;left:0;width:648px;height:284px;background:linear-gradient(180deg,var(--green-light) 10%,var(--green) 50%,var(--green-deep))}
.gummy-photo{left:0;top:8px;width:157px;height:120px;background:radial-gradient(ellipse at 40% 45%,#f29a20,#e04a28 45%,#f3c73a 70%,rgba(140,198,63,0) 85%)}
.section-title{font-family:"Montserrat",sans-serif;font-weight:700;font-size:18px;letter-spacing:.5px}
.about-title{top:108px;color:var(--white)}
.about-text{top:144px;left:100px;width:448px;font-size:6.6px;line-height:13px;color:var(--white);text-align:center}
.btn--light{left:286px;top:205px;width:76px;height:30px;line-height:30px;background:var(--white);color:var(--green-dark)}

/* gummies */
.feature{top:646px;left:0;width:648px;height:320px;background:var(--white)}
.feature-photo{left:97px;top:52px;width:145px;height:214px;background:linear-gradient(180deg,#b3934d 0,#8a7a3f 40%,#7fcb4a 60%,#9fe07a 100%);border-radius:40% 40% 20% 20%}
.heading-green{color:var(--green);font-family:"Montserrat",sans-serif;font-weight:700;font-size:18px;line-height:20px}
.heading-green .dark{color:var(--green-dark)}
.feature-head{left:334px;top:53px}
.feature-text{left:283px;top:101px;width:272px;font-size:6.6px;line-height:14.5px;text-align:justify}
.btn--small{width:69px;height:26px;line-height:26px}

/* products */
.products{top:966px;left:0;width:648px;height:532px;background:var(--grey-bg)}
.leaf-photo{left:482px;top:-54px;width:166px;height:130px;background:radial-gradient(ellipse at 60% 55%,#6fb52c,#9ad04c 40%,rgba(238,238,239,0) 72%)}
.products-head{top:47px;text-align:center}
.product{width:145px}
.product-box{width:145px;height:138px;border:1px solid #777;background:var(--white);position:relative}
.product-img{position:absolute;inset:18px;border-radius:8px}
.product-label{font-size:9.5px;font-weight:500;text-align:center;margin-top:12px}
.arrow{top:280px}

/* reviews */
.reviews{top:1498px;left:0;width:648px;height:328px;background:var(--white)}
.plant-photo{left:382px;top:50px;width:230px;height:278px;background:linear-gradient(180deg,#5e6a44,#394630 60%,#55703a);border-radius:45% 45% 10% 10%}
.reviews-head{left:145px;top:52px}
.review-title{left:93px;top:116px;font-family:"Fira Sans Condensed",sans-serif;font-size:12.5px;color:var(--green-dark);display:flex;align-items:center;gap:8px}
.review-text{left:93px;top:142px;width:278px;font-size:6.6px;line-height:14.5px;font-style:italic}
.review-author{left:93px;top:207px;font-size:6.6px;font-style:italic}
.btn--review{left:93px;top:229px}
.dots{left:93px;top:279px;display:flex;gap:5px}
.dot{width:7px;height:7px;border-radius:50%;background:var(--green-light)}
.dot.on{background:var(--green)}

/* newsletter */
.newsletter{top:1826px;left:0;width:648px;height:207px;background:linear-gradient(180deg,var(--green-light),var(--green) 45%,var(--green-deep))}
.bud-photo{left:0;top:-14px;width:142px;height:185px;background:radial-gradient(ellipse at 40% 45%,#8a8a4a,#6c7a3a 45%,rgba(140,198,63,0) 72%)}
.newsletter-title{top:44px;color:var(--white);line-height:21px}
.newsletter-text{top:97px;font-size:6.6px;color:var(--white)}
.email{left:170px;top:127px;width:307px;height:27px;border-radius:14px;background:var(--white);border:1.5px solid #dfe9d8;font-size:9px;padding:7px 10px}
.email .btn{position:absolute;right:2px;top:2px;width:64px;height:20px;line-height:20px;font-size:7px}

/* footer */
.site-footer{top:2033px;left:0;width:648px;height:354px;background:var(--footer);color:var(--white)}
.footer-brand{left:92px;top:55px;width:172px;font-family:"Fira Sans",sans-serif;font-weight:600;font-size:22px;line-height:26px;text-align:center;letter-spacing:1px;color:var(--white)}
.footer-head{top:57px;font-family:"Montserrat",sans-serif;font-weight:700;font-size:11px}
.footer-links{left:301px;top:86px;font-size:7.2px;line-height:16.3px}
.contact{left:418px;top:86px;font-size:7.2px;line-height:14px}
.contact li{list-style:none;display:flex;gap:8px;margin-bottom:8px}
.contact-ico{flex:none;width:15px;height:15px;border-radius:50%;background:var(--green);display:flex;align-items:center;justify-content:center}
.rule{left:93px;width:462px;height:1px;background:#bbb}
.disclaimer-title{top:214px;font-size:7px}
.disclaimer{top:233px;left:93px;width:462px;font-size:5.6px;line-height:11px;text-align:center}
.copyright{left:93px;top:323px;font-size:7px}
.payments{left:430px;top:321px;display:flex;gap:4px;font-size:6px}
.payments span{background:var(--white);color:var(--ink);padding:1px 3px}

/* age gate */
.shade{inset:0;background:rgba(0,0,0,.58)}
.age-gate{left:154px;top:87px;width:339px;height:259px;background:var(--white);text-align:center}
.age-brand{top:36px;font-size:18px;line-height:22px}
.age-title{top:138px;font-family:"Montserrat",sans-serif;font-weight:600;font-size:15px;color:var(--green-dark)}
.age-question{top:170px;font-size:9px}
.age-btn{top:203px;width:53px;height:24px;line-height:24px;border-radius:12px;font-size:8.5px;color:var(--white)}
.age-yes{left:113px;background:linear-gradient(180deg,var(--green),var(--green-dark))}
.age-no{left:173px;background:#555}
</style>
</head>
<body>
<div class="canvas">

<!-- Home page -->
<section class="page page--home">
  <header class="site-header abs">
    <div class="brand abs" style="left:92px;top:28px;width:95px">GREENVALE<br>CBD CO.</div>
    <div class="search abs">Search<span class="search-btn"></span></div>
    <nav class="nav abs"><span class="active">HOME</span><span>SHOP</span><span>WHOLESALE</span><span>ABOUT US</span></nav>
    <span class="icon-btn abs" style="left:504px"></span>
    <span class="icon-btn filled abs" style="left:532px"></span>
  </header>

  <div class="hero abs">
    <div class="hero-photo abs" role="img" aria-label="Tipped glass jar spilling hemp flower buds"></div>
    <h1 class="hero-title abs">GREENVALE</h1>
    <p class="hero-text abs">We believe in quality and strive to bring you the highest-grade hemp products on the market today.</p>
    <span class="btn btn--hero abs">READ MORE</span>
  </div>

  <div class="about abs">
    <svg class="abs" style="left:0;top:0" width="648" height="50" viewBox="0 0 648 50"><path d="M0 0 H648 V0 Q324 80 0 0Z" fill="#fcfcfc"/></svg>
    <div class="gummy-photo abs" role="img" aria-label="Colourful gummy bears"></div>
    <h2 class="section-title about-title abs center">ABOUT GREENVALE</h2>
    <p class="about-text abs">Nemo enim ipsam voluptatem quia voluptas sit aspernatur aut odit aut fugit, sed quia consequuntur magni dolores eos qui ratione voluptatem sequi nesciunt. Neque porro quisquam est, qui dolorem ipsum quia dolor sit amet, consectetur, adipisci velit, sed quia non numquam eius modi tempora incidunt ut labore et dolore magnam aliquam quaerat voluptatem.</p>
    <span class="btn btn--light abs">READ MORE</span>
  </div>

  <div class="feature abs">
    <div class="feature-photo abs" role="img" aria-label="Hemp bud resting on green gummy bears"></div>
    <h2 class="heading-green feature-head abs">CBD<br><span class="dark">GUMMIES/EDIBLES</span></h2>
    <div class="feature-text abs">
      <p>Nam libero tempore, cum soluta nobis est eligendi optio cumque nihil impedit quo minus id quod maxime placeat facere possimus, omnis voluptas assumenda est, omnis dolor repellendus. Temporibus autem quibusdam et aut officiis debitis aut rerum necessitatibus saepe eveniet ut et voluptates repudiandae sint et molestiae non recusandae.</p>
      <p style="margin-top:4px">Est eligendi optio cumque nihil impedit quo minus id quod maxime placeat facere possimus, omnis voluptas assumenda est, omnis dolor repellendus. Temporibus autem quibusdam.</p>
    </div>
    <span class="btn btn--small abs" style="left:283px;top:233px">READ MORE</span>
  </div>

  <div class="products abs">
    <div class="leaf-photo abs" role="img" aria-label="Hemp leaf"></div>
    <h2 class="heading-green products-head abs center">CBD<br><span class="dark">DELTA&nbsp; PRODUCTS</span></h2>
    <svg class="arrow abs" style="left:37px" width="16" height="36"><path d="M14 2 L2 18 L14 34" fill="none" stroke="#1d7a2e" stroke-width="2"/></svg>
    <svg class="arrow abs" style="left:594px" width="16" height="36"><path d="M2 2 L14 18 L2 34" fill="none" stroke="#1d7a2e" stroke-width="2"/></svg>
    <div class="product abs" style="left:94px;top:119px"><div class="product-box"><div class="product-img" role="img" aria-label="Gummy bears with hemp leaf" style="background:linear-gradient(90deg,#6fb52c,#f3b12a,#e04a28)"></div></div><p class="product-label">CBD gummies - $200</p></div>
    <div class="product abs" style="left:252px;top:119px"><div class="product-box"><div class="product-img" role="img" aria-label="Hemp flower in a glass jar" style="background:linear-gradient(180deg,#e9ece6,#8e9a6a)"></div></div><p class="product-label">Hemp flower - $250</p></div>
    <div class="product abs" style="left:409px;top:119px"><div class="product-box"><div class="product-img" role="img" aria-label="Pet with a CBD oil bottle" style="background:linear-gradient(90deg,#cbb89a,#f2efe9)"></div></div><p class="product-label">CBD for pets - $250</p></div>
    <div class="product abs" style="left:94px;top:312px"><div class="product-box" style="height:132px"><div class="product-img" role="img" aria-label="CBD vape device" style="background:linear-gradient(90deg,#f4f4f4,#9a9a9a,#f0f0f0)"></div></div><p class="product-label">CBD vapes - $250</p></div>
    <div class="product abs" style="left:252px;top:312px"><div class="product-box" style="height:132px"><div class="product-img" role="img" aria-label="Red gel capsules" style="background:radial-gradient(circle,#e04a4a,#f8dada 70%)"></div></div><p class="product-label">Capsules &amp; gel tabs - $250</p></div>
    <div class="product abs" style="left:409px;top:312px"><div class="product-box" style="height:132px"><div class="product-img" role="img" aria-label="CBD vape cartridge" style="background:radial-gradient(ellipse,#7fa3e0,#eef2fb 70%)"></div></div><p class="product-label">CBD Cartridges - $250</p></div>
  </div>

  <div class="reviews abs">
    <div class="plant-photo abs" role="img" aria-label="Flowering hemp plant"></div>
    <h2 class="heading-green reviews-head abs">OUR<br><span class="dark">PEOPLE REVIEWS</span></h2>
    <div class="review-title abs">GOOD PRODUCT
      <svg width="80" height="13" viewBox="0 0 80 13"><g fill="#3f9a2a"><path id="st" d="M6.5 0l1.9 4.2 4.6.4-3.5 3 1.1 4.5-4.1-2.4-4.1 2.4 1.1-4.5-3.5-3 4.6-.4z"/><use href="#st" x="16"/><use href="#st" x="32"/><use href="#st" x="48"/><use href="#st" x="64"/></g></svg>
    </div>
    <p class="review-text abs">Nam libero tempore, cum soluta nobis est eligendi optio cumque nihil impedit quo minus id quod maxime placeat facere possimus, omnis voluptas assumenda est, omnis dolor repellendus. Temporibus autem quibusdam et aut officiis debitis aut rerum necessitatibus.</p>
    <p class="review-author abs">- Clara, CEO</p>
    <span class="btn btn--small btn--review abs">LOAD MORE</span>
    <div class="dots abs"><span class="dot on"></span><span class="dot"></span><span class="dot"></span></div>
  </div>

  <div class="newsletter abs">
    <div class="bud-photo abs" role="img" aria-label="Close-up hemp bud"></div>
    <h2 class="section-title newsletter-title abs center">SUBSCRIBE<br>TO OUR NEWSLETTER</h2>
    <p class="newsletter-text abs center">Sign up for our email list and get 15% off your first order</p>
    <div class="email abs">Email Address<span class="btn">SUBSCRIBE</span></div>
  </div>

  <footer class="site-footer abs">
    <div class="footer-brand abs">GREENVALE<br>CBD CO.</div>
    <h3 class="footer-head abs" style="left:301px">REF LINKS</h3>
    <ul class="footer-links abs" style="list-style:none"><li>Privacy Policy</li><li>Shipping Policy</li><li>Refund Policy</li><li>Terms &amp; Conditions</li></ul>
    <h3 class="footer-head abs" style="left:418px">CONTACT US</h3>
    <ul class="contact abs">
      <li><span class="contact-ico"><svg width="8" height="8" viewBox="0 0 8 8"><path d="M1 1l2 0 1 2-1 1q1 1.5 2 2l1-1 2 1 0 2Q3 8 1 1z" fill="#fff"/></svg></span><span style="padding-top:1px">+123 456 7890</span></li>
      <li><span class="contact-ico"><svg width="9" height="7" viewBox="0 0 9 7"><rect x=".5" y=".5" width="8" height="6" fill="none" stroke="#fff"/><path d="M.5 .5l4 3 4-3" fill="none" stroke="#fff"/></svg></span><span style="padding-top:1px">info@greenvale.example</span></li>
      <li><span class="contact-ico"><svg width="7" height="9" viewBox="0 0 7 9"><path d="M3.5 9Q0 5 0 3.5a3.5 3.5 0 0 1 7 0Q7 5 3.5 9z" fill="#fff"/></svg></span><span>50, dummy city, dummy state,<br>2589635</span></li>
    </ul>
    <div class="rule abs" style="top:194px"></div>
    <p class="disclaimer-title abs center">NWB Disclaimer:</p>
    <p class="disclaimer abs">" The statements made regarding these products have not been evaluated by the National Wellness Bureau. The efficacy of these products has not been confirmed by NWB-approved research. These products are not intended to diagnose, treat, cure or prevent any disease. All information presented here is not meant as a substitute for or alternative to information from health care practitioners. Please consult your health care professional about potential interactions or other possible complications before using any product. The Federal Food, Drug, and Cosmetic Act requires this notice."</p>
    <div class="rule abs" style="top:296px"></div>
    <p class="copyright abs">Copyrights @ 2021 Greenvale. All Rights Reserved.</p>
    <div class="payments abs"><span>Tollway</span><span>Pavo</span><span>CoinRidge</span><span>Amberpay</span><span>Farreach</span></div>
  </footer>
</section>

<!-- Home page with age verification -->
<section class="page page--gate">
  <header class="site-header abs">
    <div class="brand abs" style="left:92px;top:28px;width:95px">GREENVALE<br>CBD CO.</div>
    <div class="search abs">Search<span class="search-btn"></span></div>
    <nav class="nav abs"><span class="active">HOME</span><span>SHOP</span><span>WHOLESALE</span><span>ABOUT US</span></nav>
    <span class="icon-btn abs" style="left:504px"></span>
    <span class="icon-btn filled abs" style="left:532px"></span>
  </header>

  <div class="hero abs">
    <div class="hero-photo abs" role="img" aria-label="Tipped glass jar spilling hemp flower buds"></div>
    <h1 class="hero-title abs">GREENVALE</h1>
    <p class="hero-text abs">We believe in quality and strive to bring you the highest-grade hemp products on the market today.</p>
    <span class="btn btn--hero abs">READ MORE</span>
  </div>

  <div class="about abs">
    <svg class="abs" style="left:0;top:0" width="648" height="50" viewBox="0 0 648 50"><path d="M0 0 H648 V0 Q324 80 0 0Z" fill="#fcfcfc"/></svg>
    <div class="gummy-photo abs" role="img" aria-label="Colourful gummy bears"></div>
    <h2 class="section-title about-title abs center">ABOUT GREENVALE</h2>
    <p class="about-text abs">Nemo enim ipsam voluptatem quia voluptas sit aspernatur aut odit aut fugit, sed quia consequuntur magni dolores eos qui ratione voluptatem sequi nesciunt. Neque porro quisquam est, qui dolorem ipsum quia dolor sit amet, consectetur, adipisci velit, sed quia non numquam eius modi tempora incidunt ut labore et dolore magnam aliquam quaerat voluptatem.</p>
    <span class="btn btn--light abs">READ MORE</span>
  </div>

  <div class="feature abs">
    <div class="feature-photo abs" role="img" aria-label="Hemp bud resting on green gummy bears"></div>
    <h2 class="heading-green feature-head abs">CBD<br><span class="dark">GUMMIES/EDIBLES</span></h2>
    <div class="feature-text abs">
      <p>Nam libero tempore, cum soluta nobis est eligendi optio cumque nihil impedit quo minus id quod maxime placeat facere possimus, omnis voluptas assumenda est, omnis dolor repellendus. Temporibus autem quibusdam et aut officiis debitis aut rerum necessitatibus saepe eveniet ut et voluptates repudiandae sint et molestiae non recusandae.</p>
      <p style="margin-top:4px">Est eligendi optio cumque nihil impedit quo minus id quod maxime placeat facere possimus, omnis voluptas assumenda est, omnis dolor repellendus. Temporibus autem quibusdam.</p>
    </div>
    <span class="btn btn--small abs" style="left:283px;top:233px">READ MORE</span>
  </div>

  <div class="products abs">
    <div class="leaf-photo abs" role="img" aria-label="Hemp leaf"></div>
    <h2 class="heading-green products-head abs center">CBD<br><span class="dark">DELTA&nbsp; PRODUCTS</span></h2>
    <svg class="arrow abs" style="left:37px" width="16" height="36"><path d="M14 2 L2 18 L14 34" fill="none" stroke="#1d7a2e" stroke-width="2"/></svg>
    <svg class="arrow abs" style="left:594px" width="16" height="36"><path d="M2 2 L14 18 L2 34" fill="none" stroke="#1d7a2e" stroke-width="2"/></svg>
    <div class="product abs" style="left:94px;top:119px"><div class="product-box"><div class="product-img" role="img" aria-label="Gummy bears with hemp leaf" style="background:linear-gradient(90deg,#6fb52c,#f3b12a,#e04a28)"></div></div><p class="product-label">CBD gummies - $200</p></div>
    <div class="product abs" style="left:252px;top:119px"><div class="product-box"><div class="product-img" role="img" aria-label="Hemp flower in a glass jar" style="background:linear-gradient(180deg,#e9ece6,#8e9a6a)"></div></div><p class="product-label">Hemp flower - $250</p></div>
    <div class="product abs" style="left:409px;top:119px"><div class="product-box"><div class="product-img" role="img" aria-label="Pet with a CBD oil bottle" style="background:linear-gradient(90deg,#cbb89a,#f2efe9)"></div></div><p class="product-label">CBD for pets - $250</p></div>
    <div class="product abs" style="left:94px;top:312px"><div class="product-box" style="height:132px"><div class="product-img" role="img" aria-label="CBD vape device" style="background:linear-gradient(90deg,#f4f4f4,#9a9a9a,#f0f0f0)"></div></div><p class="product-label">CBD vapes - $250</p></div>
    <div class="product abs" style="left:252px;top:312px"><div class="product-box" style="height:132px"><div class="product-img" role="img" aria-label="Red gel capsules" style="background:radial-gradient(circle,#e04a4a,#f8dada 70%)"></div></div><p class="product-label">Capsules &amp; gel tabs - $250</p></div>
    <div class="product abs" style="left:409px;top:312px"><div class="product-box" style="height:132px"><div class="product-img" role="img" aria-label="CBD vape cartridge" style="background:radial-gradient(ellipse,#7fa3e0,#eef2fb 70%)"></div></div><p class="product-label">CBD Cartridges - $250</p></div>
  </div>

  <div class="reviews abs">
    <div class="plant-photo abs" role="img" aria-label="Flowering hemp plant"></div>
    <h2 class="heading-green reviews-head abs">OUR<br><span class="dark">PEOPLE REVIEWS</span></h2>
    <div class="review-title abs">GOOD PRODUCT
      <svg width="80" height="13" viewBox="0 0 80 13"><g fill="#3f9a2a"><path id="st2" d="M6.5 0l1.9 4.2 4.6.4-3.5 3 1.1 4.5-4.1-2.4-4.1 2.4 1.1-4.5-3.5-3 4.6-.4z"/><use href="#st2" x="16"/><use href="#st2" x="32"/><use href="#st2" x="48"/><use href="#st2" x="64"/></g></svg>
    </div>
    <p class="review-text abs">Nam libero tempore, cum soluta nobis est eligendi optio cumque nihil impedit quo minus id quod maxime placeat facere possimus, omnis voluptas assumenda est, omnis dolor repellendus. Temporibus autem quibusdam et aut officiis debitis aut rerum necessitatibus.</p>
    <p class="review-author abs">- Clara, CEO</p>
    <span class="btn btn--small btn--review abs">LOAD MORE</span>
    <div class="dots abs"><span class="dot on"></span><span class="dot"></span><span class="dot"></span></div>
  </div>

  <div class="newsletter abs">
    <div class="bud-photo abs" role="img" aria-label="Close-up hemp bud"></div>
    <h2 class="section-title newsletter-title abs center">SUBSCRIBE<br>TO OUR NEWSLETTER</h2>
    <p class="newsletter-text abs center">Sign up for our email list and get 15% off your first order</p>
    <div class="email abs">Email Address<span class="btn">SUBSCRIBE</span></div>
  </div>

  <footer class="site-footer abs">
    <div class="footer-brand abs">GREENVALE<br>CBD CO.</div>
    <h3 class="footer-head abs" style="left:301px">REF LINKS</h3>
    <ul class="footer-links abs" style="list-style:none"><li>Privacy Policy</li><li>Shipping Policy</li><li>Refund Policy</li><li>Terms &amp; Conditions</li></ul>
    <h3 class="footer-head abs" style="left:418px">CONTACT US</h3>
    <ul class="contact abs">
      <li><span class="contact-ico"><svg width="8" height="8" viewBox="0 0 8 8"><path d="M1 1l2 0 1 2-1 1q1 1.5 2 2l1-1 2 1 0 2Q3 8 1 1z" fill="#fff"/></svg></span><span style="padding-top:1px">+123 456 7890</span></li>
      <li><span class="contact-ico"><svg width="9" height="7" viewBox="0 0 9 7"><rect x=".5" y=".5" width="8" height="6" fill="none" stroke="#fff"/><path d="M.5 .5l4 3 4-3" fill="none" stroke="#fff"/></svg></span><span style="padding-top:1px">info@greenvale.example</span></li>
      <li><span class="contact-ico"><svg width="7" height="9" viewBox="0 0 7 9"><path d="M3.5 9Q0 5 0 3.5a3.5 3.5 0 0 1 7 0Q7 5 3.5 9z" fill="#fff"/></svg></span><span>50, dummy city, dummy state,<br>2589635</span></li>
    </ul>
    <div class="rule abs" style="top:194px"></div>
    <p class="disclaimer-title abs center">NWB Disclaimer:</p>
    <p class="disclaimer abs">" The statements made regarding these products have not been evaluated by the National Wellness Bureau. The efficacy of these products has not been confirmed by NWB-approved research. These products are not intended to diagnose, treat, cure or prevent any disease. All information presented here is not meant as a substitute for or alternative to information from health care practitioners. Please consult your health care professional about potential interactions or other possible complications before using any product. The Federal Food, Drug, and Cosmetic Act requires this notice."</p>
    <div class="rule abs" style="top:296px"></div>
    <p class="copyright abs">Copyrights @ 2021 Greenvale. All Rights Reserved.</p>
    <div class="payments abs"><span>Tollway</span><span>Pavo</span><span>CoinRidge</span><span>Amberpay</span><span>Farreach</span></div>
  </footer>

  <div class="shade abs"></div>
  <div class="age-gate abs" role="dialog" aria-label="Age verification">
    <div class="brand age-brand abs center">GREENVALE<br>CBD CO.</div>
    <p class="age-title abs center">21+</p>
    <p class="age-question abs center">Are you of legal age at your area to purchase vaping products?</p>
    <span class="age-btn age-yes abs">YES</span>
    <span class="age-btn age-no abs">NO</span>
  </div>
</section>

</div>
</body>
</html>
```